TRV PowerPoint

I am looking for a clean, corporate PowerPoint template.

I would like the following:
- title slide
- break slide
- blank slide with title (for graphs or graphics)
- an ending slide.

Target Market(s)

Business professionals, medium to large business clients.

Requirements
Must have
• Must incorporate the TRV logo in either the header or footer

```html
<!DOCTYPE html>
<html lang="en">
<head>
<meta charset="utf-8">
<title>TRV PowerPoint Template</title>
<link href="https://fonts.googleapis.com/css2?family=Libre+Baskerville:wght@400;700&family=Open+Sans:wght@400;600&display=swap" rel="stylesheet">
<style>
:root{
  --page:#e9e9ea;
  --white:#ffffff;
  --blue:#2c53a3;
  --navy:#1b3472;
  --sky:#8fa9da;
  --pale:#d6e0f3;
  --ink:#2a2a2a;
  --muted:#555a66;
  --gold:#e9a43a;
  --yellow:#f2c230;
}
*{margin:0;padding:0;box-sizing:border-box}
html,body{width:1200px;height:3125px;overflow:hidden;background:var(--page)}
.deck{width:1200px;height:3125px;padding:14px 16px;display:grid;grid-template-columns:576px 576px;grid-auto-rows:432px;column-gap:16px;row-gap:12px}
.slide{position:relative;width:576px;height:432px;background:var(--white);overflow:hidden;box-shadow:0 1px 3px rgba(0,0,0,.25);font-family:"Libre Baskerville",Georgia,serif;color:var(--ink)}
.brand{font-family:"Open Sans",Arial,sans-serif;font-weight:600;color:var(--white);font-size:30px;letter-spacing:4px;display:flex;align-items:center;gap:10px}
.brand .mark{width:14px;height:14px;background:var(--white)}
.brand.small{font-size:14px;letter-spacing:2px;gap:6px}
.brand.small .mark{width:7px;height:7px}
.brand.on-white{color:var(--navy)}
.brand.on-white .mark{background:var(--navy)}
.brand.center{position:absolute;left:0;width:576px;justify-content:center}
.web{font-family:"Open Sans",Arial,sans-serif;font-size:10px;color:var(--pale);position:absolute;left:0;width:576px;text-align:center}
.photo{position:absolute}
.cover-top{position:absolute;left:0;top:0;width:576px;height:290px;background:linear-gradient(180deg,#3c66b8 0%,#24489a 60%,#1a3678 100%)}
.cover-photo{left:0;bottom:0;width:576px;height:175px;background:linear-gradient(180deg,#8ea6cf,#3a5994 60%,#1d3368)}
.cover-title{position:absolute;left:0;width:576px;text-align:center;color:var(--white);font-size:28px;font-weight:700;letter-spacing:1px}
.cover-sub{position:absolute;left:0;width:576px;text-align:center;color:var(--gold);font-family:"Open Sans",Arial,sans-serif;font-size:10px;font-weight:600;letter-spacing:1px}
.cover-small{position:absolute;left:0;width:576px;text-align:center;color:var(--pale);font-family:"Open Sans",Arial,sans-serif;font-size:7px;line-height:10px}
.title-band{position:absolute;left:0;top:220px;width:576px;height:212px;background:linear-gradient(180deg,#2e58aa,#1a3576)}
.marker{position:absolute;left:0;top:22px;width:18px;height:18px;background:var(--blue)}
.slide-title{position:absolute;left:40px;top:18px;width:510px;font-size:19px;font-weight:700;line-height:24px;text-transform:uppercase;color:var(--ink)}
.slide-title.narrow{width:440px}
.foot{position:absolute;left:0;bottom:0;width:576px;height:62px}
.foot svg{position:absolute;left:0;top:0}
.foot-info{position:absolute;left:14px;bottom:10px;font-family:"Open Sans",Arial,sans-serif;font-size:6px;line-height:8px;color:var(--pale)}
.foot-brand{position:absolute;left:0;width:576px;bottom:14px;justify-content:center}
.page-no{position:absolute;right:16px;bottom:12px;font-family:"Open Sans",Arial,sans-serif;font-size:9px;color:var(--white)}
.copy{position:absolute;font-size:8px;line-height:12px;color:var(--muted);text-align:justify}
.copy p+p{margin-top:10px}
.num{width:30px;height:30px;border-radius:50%;background:radial-gradient(circle at 35% 30%,#6a8fd6,var(--blue));color:var(--white);font-family:"Open Sans",Arial,sans-serif;font-size:11px;display:flex;align-items:center;justify-content:center;flex:none}
.item{display:flex;gap:14px;align-items:flex-start}
.item h4{font-size:8px;font-weight:700;color:var(--ink);margin-bottom:2px}
.item p{font-size:7px;line-height:10px;color:var(--muted)}
.list{position:absolute;left:36px;top:82px;width:480px;display:flex;flex-direction:column;gap:18px}
.grid6{position:absolute;left:40px;top:80px;width:500px;display:grid;grid-template-columns:1fr 1fr;column-gap:40px;row-gap:26px}
.trio{position:absolute;left:30px;top:76px;width:516px;display:grid;grid-template-columns:repeat(3,1fr);column-gap:20px}
.avatar{width:110px;height:110px;border-radius:50%;margin:0 auto 12px;border:3px solid var(--pale)}
.trio p{font-size:7px;line-height:10px;color:var(--muted);text-align:center}
.map{left:60px;top:80px;width:456px;height:230px;background:linear-gradient(160deg,#5c82c9,#2c53a3);border-radius:4px}
.map-note{position:absolute;left:0;top:318px;width:576px;text-align:center;font-size:8px;color:var(--muted)}
.divider-top{position:absolute;left:0;top:0;width:576px;height:300px;background:linear-gradient(180deg,#3c66b8,#1a3678)}
.chart{position:absolute}
.chart text{font-family:"Open Sans",Arial,sans-serif}
</style>
</head>
<body>
<main class="deck">

<section class="slide">
  <div class="cover-top"></div>
  <div class="brand center" style="top:112px">TRV <span class="mark"></span></div>
  <div class="web" style="top:196px">www.trvgroup.com</div>
  <div class="photo cover-photo" role="img" aria-label="Photo of two business people shaking hands"></div>
</section>

<section class="slide">
  <div class="brand on-white center" style="top:112px">TRV <span class="mark"></span></div>
  <div class="title-band"></div>
  <svg class="chart" style="left:0;top:180px" width="576" height="70" viewBox="0 0 576 70"><path d="M0 40 Q300 70 576 0 L576 70 L0 70Z" fill="#2e58aa"/><path d="M0 40 Q300 70 576 0" fill="none" stroke="#8fa9da" stroke-width="3"/></svg>
  <div class="cover-title" style="top:282px">YOUR TITTLE HERE</div>
  <div class="cover-sub" style="top:322px">YOUR PRESENTATION SUBTITLE HERE</div>
  <div class="cover-small" style="top:384px">Prepared by the strategy team for our valued clients<br>Corporate meeting, annual review</div>
</section>

<section class="slide">
  <div class="marker"></div>
  <h2 class="slide-title narrow">Optimus technology presentation powerful mission 1</h2>
  <div class="photo" style="left:48px;top:80px;width:180px;height:230px;background:linear-gradient(180deg,#9db3d8,#3c5d96)" role="img" aria-label="Photo of a glass office tower at dusk"></div>
  <div class="copy" style="left:300px;top:84px;width:250px">
    <p>The team has forged a courageous and dynamic approach to the methodology of research, by overcoming previous pitfalls that held the industry back.</p>
    <p>Essential to this approach as it overcame pitfalls that held the industry back, the group has propelled the frontier of multiple endeavours to a new level, with groundbreaking initiatives that have revolutionised the way research and development are conducted.</p>
  </div>
  <div class="foot"><svg width="576" height="62" viewBox="0 0 576 62"><path d="M0 22 Q288 0 576 16 L576 62 L0 62Z" fill="var(--blue)"/><path d="M0 22 Q288 0 576 16" fill="none" stroke="#8fa9da" stroke-width="2"/></svg><div class="foot-info">www.trvgroup.com<br>Corporate presentation 2024</div><div class="foot-brand brand small">TRV <span class="mark"></span></div><div class="page-no">1</div></div>
</section>

<section class="slide">
  <div class="marker"></div>
  <h2 class="slide-title narrow">Optimus technology presentation powerful mission 1</h2>
  <div class="photo" style="left:255px;top:76px;width:150px;height:100px;background:linear-gradient(180deg,#c9d3e3,#6f86ad)" role="img" aria-label="Photo of two colleagues working at a laptop"></div>
  <div class="copy" style="left:36px;top:190px;width:200px"><p>The team has forged a courageous and dynamic approach to the methodology of research, by overcoming previous pitfalls that held the industry back and propelled the frontier of multiple endeavours to a new level.</p></div>
  <div class="copy" style="left:425px;top:80px;width:130px"><p>The team has forged a courageous and dynamic approach to the methodology of research, by overcoming previous pitfalls.</p><p>Essential to this approach as it overcame pitfalls, the group propelled the frontier of multiple endeavours to a new level with groundbreaking initiatives.</p></div>
  <div class="foot"><svg width="576" height="62" viewBox="0 0 576 62"><path d="M0 22 Q288 0 576 16 L576 62 L0 62Z" fill="var(--blue)"/><path d="M0 22 Q288 0 576 16" fill="none" stroke="#8fa9da" stroke-width="2"/></svg><div class="foot-info">www.trvgroup.com<br>Corporate presentation 2024</div><div class="foot-brand brand small">TRV <span class="mark"></span></div><div class="page-no">2</div></div>
</section>

<section class="slide">
  <div class="marker"></div>
  <h2 class="slide-title narrow">Optimus technology presentation powerful mission 1</h2>
  <div class="list">
    <div class="item"><div class="num">1</div><div><h4>We have finalised</h4><p>Since 1990, we have supported thousands of clients from the point of planning throughout their journey with the firm.</p></div></div>
    <div class="item"><div class="num">2</div><div><h4>We have finalised</h4><p>Since 1990, we have supported thousands of clients from the point of planning throughout their journey with the firm.</p></div></div>
    <div class="item"><div class="num">3</div><div><h4>We have finalised</h4><p>Since 1990, we have supported thousands of clients from the point of planning throughout their journey with the firm.</p></div></div>
    <div class="item"><div class="num">4</div><div><h4>We have finalised</h4><p>Since 1990, we have supported thousands of clients from the point of planning throughout their journey with the firm.</p></div></div>
  </div>
  <div class="foot"><svg width="576" height="62" viewBox="0 0 576 62"><path d="M0 22 Q288 0 576 16 L576 62 L0 62Z" fill="var(--blue)"/><path d="M0 22 Q288 0 576 16" fill="none" stroke="#8fa9da" stroke-width="2"/></svg><div class="foot-info">www.trvgroup.com<br>Corporate presentation 2024</div><div class="foot-brand brand small">TRV <span class="mark"></span></div><div class="page-no">3</div></div>
</section>

<section class="slide">
  <div class="marker"></div>
  <h2 class="slide-title narrow">Optimus technology presentation powerful mission 1</h2>
  <div class="grid6">
    <div class="item"><div class="num">1</div><div><h4>We have finalised</h4><p>Since 1990, we have supported thousands of clients from the point of planning.</p></div></div>
    <div class="item"><div class="num">2</div><div><h4>We have finalised</h4><p>Since 1990, we have supported thousands of clients from the point of planning.</p></div></div>
    <div class="item"><div class="num">3</div><div><h4>We have finalised</h4><p>Since 1990, we have supported thousands of clients from the point of planning.</p></div></div>
    <div class="item"><div class="num">4</div><div><h4>We have finalised</h4><p>Since 1990, we have supported thousands of clients from the point of planning.</p></div></div>
    <div class="item"><div class="num">5</div><div><h4>We have finalised</h4><p>Since 1990, we have supported thousands of clients from the point of planning.</p></div></div>
    <div class="item"><div class="num">6</div><div><h4>We have finalised</h4><p>Since 1990, we have supported thousands of clients from the point of planning.</p></div></div>
  </div>
  <div class="foot"><svg width="576" height="62" viewBox="0 0 576 62"><path d="M0 22 Q288 0 576 16 L576 62 L0 62Z" fill="var(--blue)"/><path d="M0 22 Q288 0 576 16" fill="none" stroke="#8fa9da" stroke-width="2"/></svg><div class="foot-info">www.trvgroup.com<br>Corporate presentation 2024</div><div class="foot-brand brand small">TRV <span class="mark"></span></div><div class="page-no">4</div></div>
</section>

<section class="slide">
  <div class="marker"></div>
  <h2 class="slide-title">Powerful mission 1</h2>
  <div class="trio">
    <div><div class="avatar" style="background:linear-gradient(160deg,#d8dde6,#8a97ad)" role="img" aria-label="Portrait photo of a businesswoman"></div><p>Call us on weekdays. Our team can answer questions about your plan and guide you through every step of the process ahead.</p></div>
    <div><div class="avatar" style="background:linear-gradient(160deg,#dfe6f2,#7d93bb)" role="img" aria-label="Photo of a hand touching a digital screen"></div><p>Call us on weekdays. Our team can answer questions about your plan and guide you through every step of the process ahead.</p></div>
    <div><div class="avatar" style="background:linear-gradient(160deg,#e4dfd8,#9a8f84)" role="img" aria-label="Portrait photo of a support agent with headset"></div><p>Call us on weekdays. Our team can answer questions about your plan and guide you through every step of the process ahead.</p></div>
  </div>
  <div class="foot"><svg width="576" height="62" viewBox="0 0 576 62"><path d="M0 22 Q288 0 576 16 L576 62 L0 62Z" fill="var(--blue)"/><path d="M0 22 Q288 0 576 16" fill="none" stroke="#8fa9da" stroke-width="2"/></svg><div class="foot-info">www.trvgroup.com<br>Corporate presentation 2024</div><div class="foot-brand brand small">TRV <span class="mark"></span></div><div class="page-no">5</div></div>
</section>

<section class="slide">
  <div class="marker"></div>
  <h2 class="slide-title narrow">Optimus technology presentation powerful mission 1</h2>
  <div class="photo map" role="img" aria-label="World map in blue tones"></div>
  <div class="map-note">Use this world map as needed</div>
  <div class="foot"><svg width="576" height="62" viewBox="0 0 576 62"><path d="M0 22 Q288 0 576 16 L576 62 L0 62Z" fill="var(--blue)"/><path d="M0 22 Q288 0 576 16" fill="none" stroke="#8fa9da" stroke-width="2"/></svg><div class="foot-info">www.trvgroup.com<br>Corporate presentation 2024</div><div class="foot-brand brand small">TRV <span class="mark"></span></div><div class="page-no">6</div></div>
</section>

<section class="slide">
  <div class="divider-top"></div>
  <svg class="chart" style="left:0;top:230px" width="576" height="90" viewBox="0 0 576 90"><path d="M0 70 Q300 90 576 20 L576 90 L0 90Z" fill="#ffffff"/><path d="M0 70 Q300 90 576 20" fill="none" stroke="#8fa9da" stroke-width="3"/></svg>
  <div class="web" style="top:44px">www.trvgroup.com</div>
  <div class="cover-title" style="top:150px">DIVIDER PAGES HERE</div>
  <div class="cover-sub" style="top:190px">YOUR PRESENTATION SUBTITLE HERE</div>
  <div class="brand on-white center" style="top:340px;font-size:24px">TRV <span class="mark"></span></div>
</section>

<section class="slide">
  <div class="marker"></div>
  <h2 class="slide-title" style="width:360px">Optimus technology slide powerful mission 1</h2>
  <svg class="chart" style="left:38px;top:80px" width="500" height="100" viewBox="0 0 500 100">
    <g font-size="8" fill="#fff" text-anchor="middle" font-weight="600">
      <circle cx="60" cy="50" r="46" fill="#c4d2ec"/><text x="60" y="53">PLAN</text>
      <circle cx="150" cy="50" r="46" fill="#a9bde3" opacity=".95"/><text x="150" y="53">RESEARCH</text>
      <circle cx="240" cy="50" r="46" fill="#8aa5d8" opacity=".95"/><text x="240" y="53">DESIGN</text>
      <circle cx="330" cy="50" r="46" fill="#6a8bcb" opacity=".95"/><text x="330" y="53">DEVELOP</text>
      <circle cx="420" cy="50" r="46" fill="#4b70b9" opacity=".95"/><text x="420" y="53">TESTING</text>
    </g>
  </svg>
  <div class="copy" style="left:40px;top:200px;width:496px">
    <p>The team has forged a courageous and dynamic approach to the methodology of research, by overcoming previous pitfalls that held the industry back. The group has propelled the frontier of multiple endeavours to a new level, and the pace of results keeps rising.</p>
    <p>By overcoming previous pitfalls that held the industry back, the group propelled the frontier of multiple endeavours to a new level, and new offerings are ready for clients.</p>
  </div>
  <div class="foot"><svg width="576" height="62" viewBox="0 0 576 62"><path d="M0 22 Q288 0 576 16 L576 62 L0 62Z" fill="var(--blue)"/><path d="M0 22 Q288 0 576 16" fill="none" stroke="#8fa9da" stroke-width="2"/></svg><div class="foot-info">www.trvgroup.com<br>Corporate presentation 2024</div><div class="foot-brand brand small">TRV <span class="mark"></span></div><div class="page-no">7</div></div>
</section>

<section class="slide">
  <div class="marker"></div>
  <h2 class="slide-title" style="width:420px">Slide presentation optimus page with bullet point 1</h2>
  <div class="copy" style="left:40px;top:84px;width:220px">
    <p>The team has forged a courageous and dynamic approach to the methodology of research, by overcoming previous pitfalls that held the industry back.</p>
    <p>Essential to this approach as it overcame pitfalls, the group propelled the frontier of multiple endeavours to a new level, with groundbreaking initiatives that have revolutionised the way development is conducted. With these models the team can accelerate the pace of delivery.</p>
  </div>
  <svg class="chart" style="left:290px;top:80px" width="260" height="250" viewBox="0 0 260 250">
    <g font-size="8" fill="#fff" text-anchor="middle" font-weight="600">
      <ellipse cx="130" cy="200" rx="120" ry="34" fill="#1f3f8a"/><text x="130" y="222">TESTING</text>
      <ellipse cx="130" cy="165" rx="98" ry="28" fill="#2c53a3"/><text x="130" y="185">DEVELOP</text>
      <ellipse cx="130" cy="132" rx="78" ry="23" fill="#4a70bb"/><text x="130" y="149">DESIGN</text>
      <ellipse cx="130" cy="102" rx="58" ry="18" fill="#7894cf"/><text x="130" y="115">RESEARCH</text>
      <ellipse cx="130" cy="76" rx="38" ry="13" fill="#a8bbe2"/><text x="130" y="84">PLAN</text>
    </g>
  </svg>
  <div class="foot"><svg width="576" height="62" viewBox="0 0 576 62"><path d="M0 22 Q288 0 576 16 L576 62 L0 62Z" fill="var(--blue)"/><path d="M0 22 Q288 0 576 16" fill="none" stroke="#8fa9da" stroke-width="2"/></svg><div class="foot-info">www.trvgroup.com<br>Corporate presentation 2024</div><div class="foot-brand brand small">TRV <span class="mark"></span></div><div class="page-no">8</div></div>
</section>

<section class="slide">
  <div class="marker"></div>
  <h2 class="slide-title" style="width:420px">Slide presentation optimus page with bullet point 1</h2>
  <div class="copy" style="left:40px;top:84px;width:220px">
    <p>The team has forged a courageous and dynamic approach to the methodology of research, by overcoming previous pitfalls that held the industry back.</p>
    <p>Essential to this approach as it overcame pitfalls, the group propelled the frontier of multiple endeavours to a new level, with groundbreaking initiatives that have revolutionised the way development is conducted. With these models the team can accelerate the pace of delivery.</p>
  </div>
  <svg class="chart" style="left:290px;top:84px" width="260" height="230" viewBox="0 0 260 230">
    <circle cx="130" cy="95" r="85" fill="#2c53a3"/>
    <path d="M130 95 L130 10 A85 85 0 0 1 214 84Z" fill="var(--yellow)"/>
    <path d="M130 95 L214 84 A85 85 0 0 1 200 142Z" fill="#6f8fd0"/>
    <g font-size="7" fill="#555a66">
      <rect x="20" y="200" width="8" height="8" fill="#2c53a3"/><text x="32" y="207">Sales</text>
      <rect x="90" y="200" width="8" height="8" fill="var(--yellow)"/><text x="102" y="207">Growth</text>
      <rect x="165" y="200" width="8" height="8" fill="#6f8fd0"/><text x="177" y="207">Other</text>
    </g>
  </svg>
  <div class="foot"><svg width="576" height="62" viewBox="0 0 576 62"><path d="M0 22 Q288 0 576 16 L576 62 L0 62Z" fill="var(--blue)"/><path d="M0 22 Q288 0 576 16" fill="none" stroke="#8fa9da" stroke-width="2"/></svg><div class="foot-info">www.trvgroup.com<br>Corporate presentation 2024</div><div class="foot-brand brand small">TRV <span class="mark"></span></div><div class="page-no">9</div></div>
</section>

<section class="slide">
  <div class="marker"></div>
  <h2 class="slide-title" style="width:420px">Slide presentation optimus page with bullet point 1</h2>
  <div class="copy" style="left:40px;top:84px;width:220px">
    <p>The team has forged a courageous and dynamic approach to the methodology of research, by overcoming previous pitfalls that held the industry back.</p>
    <p>Essential to this approach as it overcame pitfalls, the group propelled the frontier of multiple endeavours to a new level, with groundbreaking initiatives that have revolutionised the way development is conducted. With these models the team can accelerate the pace of delivery.</p>
  </div>
  <svg class="chart" style="left:290px;top:90px" width="260" height="230" viewBox="0 0 260 230">
    <line x1="20" y1="190" x2="250" y2="190" stroke="#b8c3d6"/>
    <rect x="40" y="140" width="30" height="50" fill="#2c53a3"/>
    <rect x="80" y="110" width="30" height="80" fill="var(--yellow)"/>
    <rect x="120" y="80" width="30" height="110" fill="#2c53a3"/>
    <rect x="160" y="40" width="30" height="150" fill="var(--yellow)"/>
    <rect x="200" y="20" width="30" height="170" fill="#2c53a3"/>
    <g font-size="7" fill="#555a66" text-anchor="middle"><text x="55" y="204">2020</text><text x="95" y="204">2021</text><text x="135" y="204">2022</text><text x="175" y="204">2023</text><text x="215" y="204">2024</text></g>
  </svg>
  <div class="foot"><svg width="576" height="62" viewBox="0 0 576 62"><path d="M0 22 Q288 0 576 16 L576 62 L0 62Z" fill="var(--blue)"/><path d="M0 22 Q288 0 576 16" fill="none" stroke="#8fa9da" stroke-width="2"/></svg><div class="foot-info">www.trvgroup.com<br>Corporate presentation 2024</div><div class="foot-brand brand small">TRV <span class="mark"></span></div><div class="page-no">10</div></div>
</section>

<section class="slide">
  <div class="cover-top" style="height:300px"></div>
  <div class="brand center" style="top:50px;font-size:24px">TRV <span class="mark"></span></div>
  <div class="cover-title" style="top:160px">THANK YOU VERY MUCH</div>
  <div class="cover-sub" style="top:200px">YOUR PRESENTATION SUBTITLE HERE</div>
  <div class="photo cover-photo" style="height:160px" role="img" aria-label="Photo of two business people shaking hands"></div>
</section>

</main>
</body>
</html>
```